National Mission Critical Construction Contractor needs Stationery Design to make a bold statement

We are a small commercial construction company, working primarily in mission critical facilities across the U.S.. We have exciting corporate changes going an and a new logo and office space so we need new stationery. The final design should incorporate our new logo and invoke a fresh, high-tech feel while looking simple and modern.

Industry/Entity Type

Construction

Contact Information for Business Card

We are required to list our state licensing qualifications on the back of our card.

Font styles to use
Sans Serif

Requirements
Must have
• We need to have a design for second page of stationery, envelopes both standard and with a window and for a 3 x 4 notepad.

```html
<!DOCTYPE html>
<html lang="en">
<head>
<meta charset="utf-8">
<title>Crestline Construction Management – Stationery</title>
<link rel="stylesheet" href="https://fonts.googleapis.com/css2?family=Montserrat:wght@400;500;600&display=swap">
<style>
  :root {
    --blue-deep: #0c73b8;
    --blue-sky: #27a7e0;
    --green: #8dc63f;
    --paper: #ffffff;
    --stage: #c5c6c8;
    --stage-light: #d8d9db;
    --watermark: #e6eaf5;
  }
  * { box-sizing: border-box; margin: 0; padding: 0; }
  html, body { width: 1200px; height: 927px; overflow: hidden; }
  body {
    position: relative;
    font-family: "Montserrat", sans-serif;
    background: radial-gradient(ellipse at 50% 50%, var(--stage-light) 0%, var(--stage) 75%);
    border: 1px solid #555;
  }
  .sheet { position: absolute; overflow: hidden; }
  .bars { position: absolute; left: 0; right: 0; bottom: 0; display: flex; gap: 5px; }
  .bar { height: 100%; }
  .bar--sky { background: var(--blue-sky); }
  .bar--green { background: var(--green); }
  .bar--deep { background: var(--blue-deep); }
  .bar--white { background: var(--paper); }

  /* Letterhead */
  .letterhead { left: 145px; top: 48px; width: 441px; height: 568px; background: var(--paper); }
  .letterhead__header { position: absolute; left: 0; top: 0; width: 100%; height: 92px; border-bottom: 2px solid var(--blue-deep); }
  .brand { position: absolute; display: flex; align-items: center; gap: 8px; color: var(--blue-deep); }
  .brand__dot { border: 2px solid var(--blue-deep); border-radius: 50%; flex: none; }
  .brand__name { font-weight: 500; line-height: 1; }
  .brand__name span { display: block; }
  .brand__title { letter-spacing: 0.5px; }
  .brand__sub { letter-spacing: 1.6px; margin-top: 5px; }
  .letterhead .brand { left: 18px; top: 21px; }
  .letterhead .brand__dot { width: 56px; height: 56px; }
  .letterhead .brand__title { font-size: 22px; }
  .letterhead .brand__sub { font-size: 7.2px; }
  .contact { position: absolute; left: 305px; top: 19px; font-size: 9.6px; line-height: 12px; color: var(--blue-sky); list-style: none; }
  .contact li { display: flex; align-items: center; gap: 6px; }
  .contact .address { display: block; margin-bottom: 5px; }
  .contact svg { width: 7px; height: 7px; flex: none; }
  .contact b { font-weight: 600; }
  .watermark { position: absolute; left: 161px; top: 214px; width: 206px; height: 206px; border: 5px solid var(--watermark); border-radius: 50%; }
  .letterhead .bars { height: 20px; }
  .letterhead .bar--sky { width: 140px; } .letterhead .bar--green { width: 152px; } .letterhead .bar--deep { flex: 1; }

  /* Folder */
  .folder { left: 606px; top: 48px; width: 441px; height: 568px; background: var(--blue-deep); }
  .ring { position: absolute; border: 5px solid var(--paper); border-radius: 50%; }
  .folder .ring { left: 118px; top: 182px; width: 204px; height: 204px; border-width: 6px; }
  .web { position: absolute; left: 0; width: 100%; text-align: center; color: var(--paper); font-size: 11.5px; letter-spacing: 0.3px; }
  .web b { font-weight: 600; }
  .folder .web { top: 526px; }
  .folder .bars { height: 20px; }
  .folder .bar--sky { width: 140px; } .folder .bar--green { width: 152px; } .folder .bar--white { flex: 1; }

  /* Envelope front */
  .envelope-front { left: 124px; top: 642px; width: 455px; height: 236px; background: var(--paper); border-radius: 12px 12px 0 0; }
  .envelope-front__flap { position: absolute; left: 0; top: 0; width: 100%; height: 30px; background: var(--blue-deep); }
  .envelope-front .brand { left: 106px; top: 92px; }
  .envelope-front .brand__dot { width: 58px; height: 58px; }
  .envelope-front .brand__title { font-size: 22px; }
  .envelope-front .brand__sub { font-size: 7.2px; }
  .envelope-front__address { position: absolute; left: 0; width: 100%; top: 199px; text-align: center; font-size: 9.2px; color: var(--blue-deep); }
  .envelope-front .bars { height: 21px; }
  .envelope-front .bar--sky { width: 144px; } .envelope-front .bar--green { width: 158px; } .envelope-front .bar--deep { flex: 1; }

  /* Envelope back */
  .envelope-back { left: 600px; top: 670px; width: 456px; height: 208px; background: var(--blue-deep); }
  .envelope-back__flap { position: absolute; left: 0; top: 0; width: 100%; height: 30px; background: var(--blue-sky); border-radius: 0 0 12px 12px; }
  .envelope-back .ring { left: 178px; top: 72px; width: 88px; height: 88px; border-width: 3px; }
  .envelope-back .web { top: 170px; }
  .envelope-back .bars { height: 21px; }
  .envelope-back .bar--sky { width: 144px; } .envelope-back .bar--green { width: 158px; } .envelope-back .bar--white { flex: 1; }
</style>
</head>
<body>
  <section class="sheet letterhead">
    <header class="letterhead__header">
      <div class="brand">
        <div class="brand__dot"></div>
        <div class="brand__name"><span class="brand__title">CRESTLINE</span><span class="brand__sub">CONSTRUCTION MANAGEMENT</span></div>
      </div>
      <ul class="contact">
        <li class="address">418B W. Harbor Ridge Ave.<br>Fairview, TX. 75069</li>
        <li><svg viewBox="0 0 10 10"><path d="M2 1l2 2-1 1c1 1.5 2 2.5 3 3l1-1 2 2-1.5 1.5C4 9 1 6 .5 2.5z" fill="currentColor"/></svg>+1.555.204.3177</li>
        <li><svg viewBox="0 0 10 10"><rect x="1" y="2" width="8" height="6" fill="none" stroke="currentColor"/><path d="M1 2l4 3 4-3" fill="none" stroke="currentColor"/></svg>sam@crestlinebuild.com</li>
        <li><svg viewBox="0 0 10 10"><circle cx="5" cy="5" r="4" fill="none" stroke="currentColor"/><path d="M1 5h8M5 1v8" stroke="currentColor"/></svg>www.<b>crestlinebuild</b>.com</li>
      </ul>
    </header>
    <div class="watermark" aria-hidden="true"></div>
    <div class="bars"><div class="bar bar--sky"></div><div class="bar bar--green"></div><div class="bar bar--deep"></div></div>
  </section>

  <section class="sheet folder">
    <div class="ring" aria-hidden="true"></div>
    <p class="web">www.<b>crestlinebuild</b>.com</p>
    <div class="bars"><div class="bar bar--sky"></div><div class="bar bar--green"></div><div class="bar bar--white"></div></div>
  </section>

  <section class="sheet envelope-front">
    <div class="envelope-front__flap"></div>
    <div class="brand">
      <div class="brand__dot"></div>
      <div class="brand__name"><span class="brand__title">CRESTLINE</span><span class="brand__sub">CONSTRUCTION MANAGEMENT</span></div>
    </div>
    <p class="envelope-front__address">418B W. Harbor Ridge Ave. Fairview, TX. 75069</p>
    <div class="bars"><div class="bar bar--sky"></div><div class="bar bar--green"></div><div class="bar bar--deep"></div></div>
  </section>

  <section class="sheet envelope-back">
    <div class="envelope-back__flap"></div>
    <div class="ring" aria-hidden="true"></div>
    <p class="web">www.<b>crestlinebuild</b>.com</p>
    <div class="bars"><div class="bar bar--sky"></div><div class="bar bar--green"></div><div class="bar bar--white"></div></div>
  </section>
</body>
</html>
```